KRT homes
KRT homes business card/letterhead
Project: KRT homes
KRT homes - Real Estate
Creative Brief
Simple
Gregory Varnell
President
742 Birch Lane Suite 3 Walpole, MA 02047
pvarnell@krtdwellings.example
krtdwellings.example
Also need business cards for Pam Teravin Broker Cell 508.555.0187 Email: pteravin@krtdwellings.example Colleen Teravin Varnell Vice President Cell 508.555.0142 Email: colleen@krtdwellings.example
Maybe large version of logo?

```html
<!DOCTYPE html>
<html lang="en">
<head>
<meta charset="utf-8">
<title>KRT homes stationery</title>
<link href="https://fonts.googleapis.com/css2?family=Roboto:wght@400;700&display=swap" rel="stylesheet">
<style>
:root{
  --backdrop:#8d8f91;
  --backdrop-light:#a9abad;
  --paper:#ffffff;
  --brand-orange:#c8470f;
  --charcoal:#3d3f42;
  --ink:#6b6b6b;
  --watermark:#f0f1f3;
}
*{margin:0;padding:0;box-sizing:border-box}
html,body{width:1200px;height:626px;overflow:hidden}
body{
  position:relative;
  background:radial-gradient(ellipse at 50% 45%,var(--backdrop-light),var(--backdrop) 75%);
  font-family:"Roboto",Arial,sans-serif;
}
.sheet{position:absolute;background:var(--paper);box-shadow:0 3px 8px rgba(0,0,0,.3);overflow:hidden}
.brand-name{
  font-weight:400;color:var(--charcoal);text-transform:uppercase;letter-spacing:.18em;
  white-space:nowrap;display:flex;align-items:center;gap:8px;line-height:1;
}
.brand-name .mark{display:inline-block;background:var(--brand-orange);flex:none}
.fine{font-size:5px;line-height:7px;color:var(--ink);white-space:nowrap}

/* business card front */
.card-front{left:34px;top:197px;width:168px;height:105px}
.card-front .brand-name{position:absolute;left:0;right:0;top:40px;justify-content:center;font-size:12px}
.card-front .brand-name .mark{width:7px;height:7px}
.card-front .fine{position:absolute;left:0;right:0;top:62px;text-align:center}

/* business card back */
.card-back{left:34px;top:319px;width:168px;height:108px;background:var(--brand-orange)}
.card-back .name-band{position:absolute;left:0;right:0;top:19px;height:16px;background:var(--paper);display:flex;flex-direction:column;align-items:center;justify-content:center}
.card-back .name-band .fine{color:var(--charcoal);line-height:6px}
.card-back .brand-name{position:absolute;left:14px;top:45px;font-size:11px;color:var(--paper)}
.card-back .brand-name .mark{width:6px;height:6px;background:var(--paper)}
.card-back .details{position:absolute;left:14px;top:64px}
.card-back .details .fine{color:var(--paper)}

/* letterhead */
.letterhead{left:233px;top:29px;width:417px;height:561px}
.letterhead .top-band{position:absolute;left:0;right:0;top:0;height:12px;background:var(--brand-orange)}
.letterhead .brand-name{position:absolute;left:0;right:0;top:44px;justify-content:center;font-size:14px}
.letterhead .brand-name .mark{width:9px;height:9px}
.letterhead .watermark{position:absolute;left:0;right:0;top:262px;text-align:center;font-size:40px;font-weight:400;text-transform:uppercase;letter-spacing:.18em;color:var(--watermark);white-space:nowrap}
.letterhead .bottom-band{position:absolute;left:0;right:0;bottom:0;height:17px;background:var(--brand-orange);display:flex;align-items:center;justify-content:center}
.letterhead .bottom-band .fine{color:var(--paper)}

/* envelope back */
.envelope-back{left:679px;top:79px;width:485px;height:235px;background:var(--brand-orange)}
.envelope-back svg{position:absolute;left:0;top:0}

/* envelope front */
.envelope-front{left:679px;top:341px;width:485px;height:216px}
.envelope-front .top-band{position:absolute;left:0;right:0;top:0;height:13px;background:var(--brand-orange)}
.envelope-front .brand-name{position:absolute;left:0;right:0;top:54px;justify-content:center;font-size:14px}
.envelope-front .brand-name .mark{width:9px;height:9px}
.envelope-front .footer-rule{position:absolute;left:0;right:0;bottom:18px;height:2px;background:var(--brand-orange)}
.envelope-front .footer{position:absolute;left:0;right:0;bottom:6px;text-align:center}
</style>
</head>
<body>

<section class="sheet card-front">
  <div class="brand-name"><span class="mark"></span>KRT homes</div>
  <p class="fine">krtdwellings.example</p>
</section>

<section class="sheet card-back">
  <div class="name-band">
    <p class="fine">Gregory Varnell</p>
    <p class="fine">President</p>
  </div>
  <div class="brand-name"><span class="mark"></span>KRT homes</div>
  <div class="details">
    <p class="fine">742 Birch Lane Suite 3 Walpole, MA 02047</p>
    <p class="fine">pvarnell@krtdwellings.example</p>
  </div>
</section>

<section class="sheet letterhead">
  <div class="top-band"></div>
  <div class="brand-name"><span class="mark"></span>KRT homes</div>
  <div class="watermark" aria-hidden="true">KRT homes</div>
  <div class="bottom-band">
    <p class="fine">T 508.555.0187 &nbsp;|&nbsp; F 508.555.0142 &nbsp;|&nbsp; pvarnell@krtdwellings.example &nbsp;|&nbsp; krtdwellings.example &nbsp;|&nbsp; 742 Birch Lane Suite 3 Walpole, MA 02047</p>
  </div>
</section>

<section class="sheet envelope-back">
  <svg width="485" height="235" viewBox="0 0 485 235" aria-hidden="true">
    <polyline points="0,0 242,105 485,0" fill="none" stroke="rgba(255,255,255,.85)" stroke-width="2"/>
  </svg>
</section>

<section class="sheet envelope-front">
  <div class="top-band"></div>
  <div class="brand-name"><span class="mark"></span>KRT homes</div>
  <div class="footer-rule"></div>
  <p class="fine footer">T 508.555.0187 &nbsp;|&nbsp; F 508.555.0142 &nbsp;|&nbsp; pvarnell@krtdwellings.example &nbsp;|&nbsp; 742 Birch Lane Suite 3 Walpole, MA 02047</p>
</section>

</body>
</html>
```